Home page design for Drone video business (the Business focusses on home videos for realtors)

Dear reader,

*I NEED DESIGNS OF ALL THE PAGES*
We need a first design of a homepage and of 4 other pages of the website of a business that sells drone video services. All the pages will need to be in the similar design style.
The video's are targeted at consumers that want to sell there home and would like to have a cool drone video of photos of their home.

How does the website look:
- has a navbar on top
- A cool looking banner of an areal drone.
- A Big header: with company name: SkyNestReels
- A smaller subheader: We film your home to increase your chances of sale
- Then a section with a Big header: How does it work
- In this section a place for a vimeo explainitory video
- Then a similar navbar styled bar with a phone number and a email address
- Then a section where the videos porfolio is displayed in a cool way
- Inside this sectiona header: Our work

- A section with header: Why us?
- 4 symbols here with a subheader and some lorum ipsum text underneath (see wireframe images)

- Under that a: Contact us
- where you can put in name, email, phone, message box and a send button

- At the bottom a footer with phone number and a fake address for now.

Be creative. Use creative but serious color.
Use a serious font. Make it a sharp design. Sharp lines. Not to dark design and not to light design.

The wireframes are the same kind of images.
PLEASE PUT IN DESIGNS OF ALL THE PAGES

Good luck

Target Market(s)

People that want to sell home and want to make a cool drone video or photos of their home.

Industry/Entity Type

Business

Contact Information for Business Card

Milo Brenning
milo@skynestreels.example
+31647283915

Logo Text

SkyNestReels

Number of Pages Required

1 page

Font styles to use
Sans Serif

Requirements
Must have
• All the sections as explained in the instructions.
• The nav bar should have an about us, services, portfolio and a contact us buttons.
• See instruction for details.
• Must include designs of the front page, contact us, our services, portfolio and contact us.
• If you do add some designs for the "about us", "services", "prices", "portfolio" and "contact us" pages, you make a way better chance of winning the competition.
Nice to have
• designs for the other pages as described at the Must haves. You make a better chance of winning if you include them. Look at the wireframes to see the mockups for those pages. think creative about what kind of sections and design should be included in those pages.
Should not have
• bad designs.

```html
<!DOCTYPE html>
<html lang="en">
<head>
<meta charset="utf-8">
<title>SkyNestReels – Home</title>
<link rel="stylesheet" href="https://fonts.googleapis.com/css2?family=Montserrat:wght@400;500;600;700&family=Open+Sans:wght@400;600;700&display=swap">
<style>
:root{
  --navy:#1d5c9a;
  --blue:#2a9fd8;
  --bright:#1e88e5;
  --icon-top:#4aa6f0;
  --icon-bottom:#1565c0;
  --text:#333;
  --line:#7fb6e0;
  --bar:#f1f2f3;
  --shadow:rgba(0,0,0,.18);
}
*{margin:0;padding:0;box-sizing:border-box}
html,body{width:1200px;height:2230px;overflow:hidden;background:#fff}
body{font-family:"Open Sans",Arial,sans-serif;color:var(--text);position:relative}
.page{position:absolute;left:72px;top:0;width:1065px;height:2230px;background:#fff;box-shadow:0 0 8px var(--shadow)}
.abs{position:absolute}
.top-rule{left:0;top:0;width:100%;height:7px;background:var(--bright)}
.brand{font-family:"Montserrat",sans-serif;font-weight:700;color:var(--navy);font-size:30px;letter-spacing:.5px}
.site-header .brand{left:25px;top:30px}
.main-nav{font-family:"Montserrat",sans-serif;font-size:21px;color:var(--blue)}
.main-nav a{position:absolute;top:37px;color:inherit;text-decoration:none;white-space:nowrap}
.main-nav a.current{color:var(--navy)}
.hero{left:0;top:97px;width:100%;height:394px;border-bottom:4px solid var(--bright);
  background:
    radial-gradient(ellipse 220px 70px at 300px 60px,rgba(255,255,255,.75),rgba(255,255,255,0)),
    radial-gradient(ellipse 260px 90px at 620px 20px,rgba(255,255,255,.7),rgba(255,255,255,0)),
    radial-gradient(ellipse 240px 110px at 860px 300px,rgba(255,255,255,.85),rgba(255,255,255,0)),
    radial-gradient(ellipse 200px 80px at 150px 330px,rgba(255,255,255,.6),rgba(255,255,255,0)),
    radial-gradient(ellipse 150px 60px at 960px 150px,rgba(255,255,255,.7),rgba(255,255,255,0)),
    linear-gradient(100deg,#0a5cf0 0%,#2a86f2 45%,#6fb4f6 80%,#a5d2fa 100%)}
.hero-roof{left:0;top:0}
.hero-card{left:309px;top:177px;width:441px;height:141px;background:rgba(255,255,255,.82);text-align:center;font-family:"Montserrat",sans-serif}
.hero-card h1{font-weight:500;font-size:36px;color:var(--navy);margin-top:27px;line-height:1.1}
.hero-card p{font-size:21px;color:var(--blue);line-height:25px;margin-top:6px}
.dots span{position:absolute;top:355px;width:46px;height:3px;background:#fff}
.dots span.on{background:#2b4e78}
.section-title{width:100%;left:0;text-align:center;font-family:"Montserrat",sans-serif;font-weight:500;font-size:36px;color:var(--navy)}
.video{left:192px;top:584px;width:676px;height:353px;
  background:
    radial-gradient(ellipse 90px 200px at 40px 90px,rgba(60,95,50,.9),rgba(60,95,50,0)),
    radial-gradient(ellipse 90px 160px at 650px 150px,rgba(70,100,60,.85),rgba(70,100,60,0)),
    linear-gradient(180deg,#b9d2e6 0%,#dfe5e8 18%,#e9ecec 30%,#5c6466 42%,#4a5253 60%,#6d7676 75%,#2f3536 100%)}
.video .play{left:303px;top:158px;width:75px;height:52px;border-radius:8px;background:var(--bright)}
.video .controls{left:0;bottom:0;width:100%;height:28px;background:rgba(20,20,20,.75)}
.video .side{right:6px;top:4px}
.contact-bar{left:0;top:951px;width:100%;height:66px;background:linear-gradient(#fafafa,var(--bar));font-family:"Open Sans",sans-serif}
.contact-bar strong{display:block;font-size:15px;color:var(--navy);font-weight:700}
.contact-bar small{font-size:13px;color:var(--blue)}
.thumb{top:1125px;width:222px;height:174px}
.thumb .play{left:83px;top:70px;width:52px;height:34px;border-radius:6px;background:var(--bright)}
.t-a{background:linear-gradient(180deg,#8dbbe4 0%,#d9e4ee 22%,#e8dcc4 35%,#c98f6a 42%,#e6d9c0 55%,#a99e87 75%,#4f5d44 100%)}
.t-b{background:linear-gradient(180deg,#8aa08a 0%,#d8e0e4 25%,#c3cacd 50%,#9aa59a 75%,#6f7f66 100%)}
.t-c{background:linear-gradient(180deg,#6fa6df 0%,#b9cde0 25%,#8fae6a 45%,#6f9a48 70%,#5a8636 100%)}
.arrow{top:1195px}
.feature{width:390px}
.feature h3{font-family:"Montserrat",sans-serif;font-weight:500;font-size:25px;color:var(--navy);line-height:30px}
.feature p{font-size:17.5px;letter-spacing:.35px;line-height:21px;text-align:justify;color:var(--text)}
.feature-icon{width:80px;height:80px;border-radius:50%;background:radial-gradient(circle at 40% 30%,var(--icon-top),var(--icon-bottom))}
.field{border:2px solid var(--line);background:#fff;font-size:14px;color:#777;padding:11px 10px}
.send{left:762px;top:2047px;width:114px;height:42px;background:linear-gradient(#4fb0e3,#2f90c8);color:#fff;font-family:"Montserrat",sans-serif;font-weight:600;font-size:18px;text-align:center;line-height:42px}
.to-top{left:1024px;top:2098px;width:48px;height:48px;border-radius:50%;background:var(--bright);z-index:2}
.site-footer{left:0;top:2133px;width:100%;height:97px;background:linear-gradient(#ffffff,#e2e2e2);box-shadow:0 -3px 6px rgba(0,0,0,.08)}
.site-footer p{position:absolute;left:85px;font-size:14px;color:var(--navy)}
.site-footer .brand{left:835px;top:32px;font-size:28px}
</style>
</head>
<body>
<div class="page">
  <div class="abs top-rule"></div>

  <header class="site-header">
    <div class="abs brand">SkyNestReels</div>
    <nav class="main-nav">
      <a class="current" style="left:516px">Services</a>
      <a style="left:648px">About Us</a>
      <a style="left:789px">Portfolio</a>
      <a style="left:913px">Contact Us</a>
    </nav>
  </header>

  <section class="abs hero" role="img" aria-label="Aerial drone flying through a bright blue sky with white clouds">
    <svg class="abs hero-roof" width="1065" height="394" viewBox="0 0 1065 394">
      <polyline points="310,178 535,84 750,178" fill="none" stroke="#fff" stroke-width="12" stroke-linejoin="miter"/>
    </svg>
    <div class="abs hero-card">
      <h1>SkyNestReels</h1>
      <p>We Film your Home to Increase<br>your chance of Sale</p>
    </div>
    <div class="dots">
      <span class="on" style="left:384px"></span>
      <span style="left:445px"></span>
      <span style="left:508px"></span>
      <span style="left:570px"></span>
    </div>
  </section>

  <h2 class="abs section-title" style="top:528px">How does it work ?</h2>
  <div class="abs video" role="img" aria-label="Explainer video still of a modern white house with driveway">
    <div class="abs play"><svg width="75" height="52"><polygon points="31,16 31,36 47,26" fill="#fff"/></svg></div>
    <svg class="abs side" width="24" height="100">
      <rect x="0" y="0" width="24" height="20" rx="2" fill="#3a3f44"/>
      <rect x="0" y="26" width="24" height="20" rx="2" fill="#3a3f44"/>
      <rect x="0" y="52" width="24" height="20" rx="2" fill="#3a3f44"/>
      <polygon points="6,90 19,82 14,96" fill="#ddd"/>
    </svg>
    <div class="abs controls">
      <svg width="676" height="28">
        <polygon points="24,8 24,20 34,14" fill="#ddd"/>
        <rect x="60" y="12" width="530" height="4" fill="#555"/>
        <rect x="60" y="12" width="75" height="4" fill="#2a9fd8"/>
        <text x="610" y="19" fill="#fff" font-size="11" font-family="Open Sans, sans-serif" font-weight="700">HD</text>
      </svg>
    </div>
  </div>

  <div class="abs contact-bar">
    <svg class="abs" style="left:66px;top:20px" width="30" height="28" viewBox="0 0 24 24"><path fill="#2a9fd8" d="M6.6 10.8a15 15 0 0 0 6.6 6.6l2.2-2.2c.3-.3.7-.4 1-.2 1.1.4 2.3.6 3.6.6.6 0 1 .4 1 1V20c0 .6-.4 1-1 1A17 17 0 0 1 3 4c0-.6.4-1 1-1h3.5c.6 0 1 .4 1 1 0 1.3.2 2.5.6 3.6.1.3 0 .7-.2 1z"/></svg>
    <div class="abs" style="left:105px;top:16px"><strong>Call US</strong><small>+31647283915</small></div>
    <svg class="abs" style="left:770px;top:22px" width="44" height="28" viewBox="0 0 44 28"><rect width="44" height="28" fill="#2a9fd8"/><polyline points="1,1 22,16 43,1" fill="none" stroke="#fff" stroke-width="2"/><line x1="1" y1="27" x2="16" y2="12" stroke="#fff" stroke-width="2"/><line x1="43" y1="27" x2="28" y2="12" stroke="#fff" stroke-width="2"/></svg>
    <div class="abs" style="left:828px;top:18px"><strong>Eamil Us</strong><small>contact@skynestreels.example</small></div>
  </div>

  <h2 class="abs section-title" style="top:1063px">Our Work</h2>
  <div class="abs thumb t-c" style="left:0;width:18px" role="img" aria-label="Portfolio video thumbnail, cropped"></div>
  <div class="abs thumb t-a" style="left:45px" role="img" aria-label="Aerial video of a Mediterranean-style villa"><div class="abs play"><svg width="52" height="34"><polygon points="21,10 21,24 32,17" fill="#fff"/></svg></div></div>
  <div class="abs thumb t-b" style="left:297px" role="img" aria-label="Drone shot over a suburban house"><div class="abs play"><svg width="52" height="34"><polygon points="21,10 21,24 32,17" fill="#fff"/></svg></div></div>
  <div class="abs thumb t-c" style="left:549px" role="img" aria-label="Aerial view of a country house in green fields"><div class="abs play"><svg width="52" height="34"><polygon points="21,10 21,24 32,17" fill="#fff"/></svg></div></div>
  <div class="abs thumb t-a" style="left:801px" role="img" aria-label="Aerial video of a villa with red tiled roof"><div class="abs play"><svg width="52" height="34"><polygon points="21,10 21,24 32,17" fill="#fff"/></svg></div></div>
  <div class="abs thumb t-c" style="left:1045px;width:18px" role="img" aria-label="Portfolio video thumbnail, cropped"></div>

  <h2 class="abs section-title" style="top:1353px">Why Us</h2>

  <div class="abs feature-icon" style="left:31px;top:1417px"><svg width="80" height="80"><text x="40" y="55" text-anchor="middle" fill="#fff" font-size="46" font-family="Open Sans, sans-serif">$</text></svg></div>
  <div class="abs feature" style="left:126px;top:1407px"><h3>Cheap</h3><p>It is a long established fact that a reader will be distracted by the readable content of a page when looking at its layout. The point of using Lorem Ipsum is that it has a more-or-less normal distribution of letters, as opposed to using 'Content here, content here', making it look like readable English.</p></div>

  <div class="abs feature-icon" style="left:551px;top:1417px"><svg width="80" height="80" fill="#fff"><polygon points="22,22 36,22 22,36"/><polygon points="58,22 44,22 58,36"/><polygon points="22,58 36,58 22,44"/><polygon points="58,58 44,58 58,44"/><g stroke="#fff" stroke-width="4"><line x1="26" y1="26" x2="34" y2="34"/><line x1="54" y1="26" x2="46" y2="34"/><line x1="26" y1="54" x2="34" y2="46"/><line x1="54" y1="54" x2="46" y2="46"/></g></svg></div>
  <div class="abs feature" style="left:645px;top:1407px"><h3>Flexible</h3><p>It is a long established fact that a reader will be distracted by the readable content of a page when looking at its layout. The point of using Lorem Ipsum is that it has a more-or-less normal distribution of letters, as opposed to using 'Content here, content here', making it look like readable English.</p></div>

  <div class="abs feature-icon" style="left:31px;top:1630px"><svg width="80" height="80"><text x="40" y="50" text-anchor="middle" fill="#fff" font-size="30" font-weight="700" font-family="Montserrat, sans-serif">4K</text></svg></div>
  <div class="abs feature" style="left:126px;top:1620px"><h3>4K Quality</h3><p>It is a long established fact that a reader will be distracted by the readable content of a page when looking at its layout. The point of using Lorem Ipsum is that it has a more-or-less normal distribution of letters, as opposed to using 'Content here, content here', making it look like readable English.</p></div>

  <div class="abs feature-icon" style="left:551px;top:1630px"><svg width="80" height="80" fill="#fff"><rect x="20" y="48" width="7" height="10"/><rect x="30" y="43" width="7" height="15"/><rect x="40" y="37" width="7" height="21"/><rect x="50" y="30" width="7" height="28"/><polyline points="20,40 34,32 42,28 56,18" fill="none" stroke="#fff" stroke-width="3"/><polygon points="51,15 60,15 58,23"/></svg></div>
  <div class="abs feature" style="left:643px;top:1620px"><h3>Increase Sale Chance</h3><p>It is a long established fact that a reader will be distracted by the readable content of a page when looking at its layout. The point of using Lorem Ipsum is that it has a more-or-less normal distribution of letters, as opposed to using 'Content here, content here', making it look like readable English.</p></div>

  <h2 class="abs section-title" style="top:1852px">Contact Us</h2>
  <form>
    <div class="abs field" style="left:190px;top:1924px;width:336px;height:43px">Name</div>
    <div class="abs field" style="left:190px;top:1985px;width:336px;height:43px">Email</div>
    <div class="abs field" style="left:190px;top:2047px;width:336px;height:43px">Phone</div>
    <div class="abs field" style="left:541px;top:1924px;width:336px;height:103px">Message</div>
    <div class="abs send">Send</div>
  </form>

  <div class="abs to-top"><svg width="48" height="48"><polyline points="15,29 24,20 33,29" fill="none" stroke="#fff" stroke-width="5"/></svg></div>

  <footer class="abs site-footer">
    <svg class="abs" style="left:68px;top:30px" width="12" height="16" viewBox="0 0 12 16"><path fill="#2a9fd8" d="M6 0a6 6 0 0 0-6 6c0 4.5 6 10 6 10s6-5.5 6-10a6 6 0 0 0-6-6zm0 8.5A2.5 2.5 0 1 1 6 3.5a2.5 2.5 0 0 1 0 5z"/></svg>
    <p style="top:28px">48 Harbour Lane, Northvale, NSW 2001 Australia</p>
    <svg class="abs" style="left:67px;top:55px" width="13" height="13" viewBox="0 0 24 24"><path fill="#2a9fd8" d="M6.6 10.8a15 15 0 0 0 6.6 6.6l2.2-2.2c.3-.3.7-.4 1-.2 1.1.4 2.3.6 3.6.6.6 0 1 .4 1 1V20c0 .6-.4 1-1 1A17 17 0 0 1 3 4c0-.6.4-1 1-1h3.5c.6 0 1 .4 1 1 0 1.3.2 2.5.6 3.6.1.3 0 .7-.2 1z"/></svg>
    <p style="top:52px">+31647283915</p>
    <div class="abs brand">SkyNestReels</div>
  </footer>
</div>

<svg class="abs arrow" style="left:33px" width="22" height="30"><polyline points="18,3 6,15 18,27" fill="none" stroke="#333" stroke-width="6"/></svg>
<svg class="abs arrow" style="left:1152px" width="22" height="30"><polyline points="4,3 16,15 4,27" fill="none" stroke="#333" stroke-width="6"/></svg>
</body>
</html>
```